Harbor of Kitchencraft Podcast Episode Cover

I’m looking for a clean, professional, and eye-catching podcast episode cover template for my show, Harbor of Kitchencraft. Each week, I feature a new guest, so the design must allow me (or my team) to easily swap in a new guest’s photo without needing advanced design skills.

The template should be:

- Drag-and-drop friendly: simple for me to replace the guest’s headshot in Canva, Photoshop, or similar.
- On-brand with the Harbor of Kitchencraft podcast: professional yet approachable, foodservice industry-focused.
- Bold and attention-grabbing for podcast platforms and social media.

Readable text at small sizes, since covers are often viewed as thumbnails.

Design Elements to Include:

1. Podcast Title: “Harbor of Kitchencraft” (prominently displayed)
2. Subtitle/Space: Line for guest’s name, professional title, and company name
3. Photo Placeholder: Large, central area where I can easily drag and drop a guest photo
4. Brand Colors: attached
5. Clean, modern fonts (easy to read at thumbnail size)
6. Background graphics or patterns that give a sense of foodservice, leadership, or nationwide reach... but do not overpower the guest photo

Format Requirements:

- Editable source file (PSD, Canva template, or layered AI/INDD)
- JPG/PNG exports for immediate use
- Square format (3000x3000px) for podcast platforms

Style Inspiration:
Think modern podcast covers: bold fonts, clean lines, professional with a touch of energy.

Deliverables:

1. Final episode cover template (editable file)
2. Instructions or guidance on how to swap out guest photos

```html
<!DOCTYPE html>
<html lang="en">
<head>
<meta charset="utf-8">
<title>Harbor of Kitchencraft – Episode Cover</title>
<link rel="stylesheet" href="https://fonts.googleapis.com/css2?family=Bebas+Neue&family=Montserrat:wght@400;700&display=swap">
<style>
  :root {
    --navy: #1d3a52;
    --gold: #f6b817;
    --ring: #e3a934;
    --white: #ffffff;
    --photo-light: #c9ccd3;
    --photo-dark: #8e929b;
  }
  html, body {
    margin: 0;
    padding: 0;
    width: 1200px;
    height: 1200px;
    overflow: hidden;
    background: var(--navy);
  }
  .cover {
    position: relative;
    width: 1200px;
    height: 1200px;
    background: var(--navy);
    overflow: hidden;
  }
  .cover-art {
    position: absolute;
    left: 0;
    top: 0;
    width: 1200px;
    height: 1200px;
  }
  .title-line {
    font-family: "Bebas Neue", "Oswald", sans-serif;
  }
  .title-line--top { fill: var(--white); }
  .title-line--bottom { fill: var(--gold); }
  .guest-text {
    font-family: "Montserrat", "Helvetica Neue", Arial, sans-serif;
    fill: var(--white);
  }
  .guest-name { font-size: 76px; font-weight: 700; }
  .guest-role { font-size: 40px; font-weight: 400; }
  .guest-company { font-size: 40px; font-weight: 700; }
</style>
</head>
<body>
  <main class="cover">
    <svg class="cover-art" viewBox="0 0 1200 1200">
      <defs>
        <linearGradient id="guest-photo-tone" x1="0" y1="0" x2="1" y2="1">
          <stop offset="0" stop-color="#c9ccd3"/>
          <stop offset="1" stop-color="#8e929b"/>
        </linearGradient>
      </defs>

      <g class="show-title" aria-label="Harbor of Kitchencraft">
        <text class="title-line title-line--top" x="165" y="332" font-size="290" textLength="871" lengthAdjust="spacingAndGlyphs">HARBOR OF</text>
        <text class="title-line title-line--bottom" x="100" y="549" font-size="244" textLength="1001" lengthAdjust="spacingAndGlyphs">KITCHENCRAFT</text>
      </g>

      <g class="guest-info">
        <text class="guest-text guest-name" x="109" y="919">Theo Marsh</text>
        <text class="guest-text guest-role" x="109" y="981">CEO &amp; Sustainability Lead</text>
        <text class="guest-text guest-company" x="109" y="1037">GreenLadle Works</text>
      </g>

      <g class="guest-frame">
        <circle class="guest-ring" cx="1006" cy="919" r="351" fill="#e3a934"/>
        <circle class="guest-photo" cx="1046" cy="927" r="340" fill="url(#guest-photo-tone)" role="img" aria-label="Guest headshot placeholder"/>
      </g>
    </svg>
  </main>
</body>
</html>
```